Mental Health & Addiction Podcast Art

Project: Podcast Cover Art / Visual Identity
Podcast Name: The Mending Path
Focus: Recovery from substance use and mental health
Objectives
Create compelling podcast artwork that:
Reflects the themes of hope, healing, and personal growth
Establishes credibility and professionalism
Appeals to individuals seeking recovery resources and support
Maintains strong brand consistency with Larkspur Wellness
Brand Integration Requirements
Logo incorporation: Integrate an element from the Larkspur Wellness Logo—potentially an abstract or partial use of the sun motif
Flexibility: Open to creative interpretations (e.g., sun rays as background texture, sunrise gradient, partial sun as a design accent)
Mandatory: Must adhere to existing Larkspur Wellness brand guidelines (approved color palette, typography, and visual style)

Target Market(s)

United states, people with addiction and mental health disorders.

Industry/Entity Type

Wellness

Font styles to use
Other font styles liked:
• See Brand Guide

Requirements
Must have
• Match brand guide, in corporate elements of the Larkspur Wellness Logo icon

```html
<!DOCTYPE html>
<html lang="en">
<head>
<meta charset="utf-8">
<title>The Mending Path — Podcast Cover</title>
<link rel="stylesheet" href="https://fonts.googleapis.com/css2?family=Roboto+Serif:opsz,wght@8..144,500;8..144,600&display=swap">
<style>
  :root {
    --navy: #02475f;
    --navy-soft: #0d5a75;
    --amber: #f6aa0f;
    --amber-glow: rgba(246, 170, 15, 0);
    --mist: #d3e7f0;
    --white: #ffffff;
  }
  html, body {
    margin: 0;
    padding: 0;
    width: 1200px;
    height: 1200px;
    overflow: hidden;
    background: var(--navy);
  }
  .cover {
    position: relative;
    width: 1200px;
    height: 1200px;
    background: var(--navy);
    overflow: hidden;
    font-family: "Roboto Serif", Georgia, serif;
  }
  .cover-shapes {
    position: absolute;
    inset: 0;
    width: 1200px;
    height: 1200px;
  }
  .frame-line {
    fill: none;
    stroke: var(--amber);
    stroke-width: 6;
    stroke-linecap: round;
  }
  .wave { fill: var(--mist); }
  .chevron {
    fill: none;
    stroke: var(--amber);
    stroke-width: 9;
    stroke-linecap: round;
    stroke-linejoin: round;
  }
  .sun-accent {
    position: absolute;
    left: 800px;
    top: 57px;
    width: 352px;
    height: 352px;
    border-top-right-radius: 34px;
    background: radial-gradient(circle at 100% 0%, var(--amber) 0%, var(--amber) 22%, rgba(246,170,15,0.55) 48%, var(--amber-glow) 72%);
  }
  .podcast-title {
    position: absolute;
    left: 118px;
    top: 98px;
    margin: 0;
    color: var(--white);
    font-weight: 600;
    font-size: 156px;
    line-height: 190px;
    letter-spacing: -1px;
  }
  .podcast-title span { display: block; }
  .listener-figure {
    position: absolute;
    left: 640px;
    top: 600px;
    width: 480px;
    height: 600px;
    border-radius: 60% 45% 30% 50% / 40% 35% 0 0;
    background: linear-gradient(165deg, var(--navy) 0%, var(--navy-soft) 55%, rgba(13,90,117,0.35) 100%);
  }
  .brand-signoff {
    position: absolute;
    left: 90px;
    top: 1046px;
    display: flex;
    align-items: center;
    gap: 16px;
  }
  .brand-dot {
    width: 46px;
    height: 46px;
    border-radius: 50%;
    background: var(--amber);
  }
  .brand-name {
    color: var(--navy);
    font-weight: 500;
    font-size: 38px;
    letter-spacing: 0.5px;
  }
</style>
</head>
<body>
  <main class="cover">
    <svg class="cover-shapes" viewBox="0 0 800 800" aria-hidden="true">
      <path class="frame-line" d="M38,600 V60 Q38,38 60,38 H745 Q767,38 767,60 V440"/>
      <path class="wave" d="M0,622 C150,598 300,612 430,520 S640,340 800,325 L800,800 L0,800 Z"/>
      <g class="chevrons">
        <polyline class="chevron" points="84,488 122,472 160,488"/>
        <polyline class="chevron" points="84,515 122,499 160,515"/>
        <polyline class="chevron" points="84,542 122,526 160,542"/>
      </g>
    </svg>

    <div class="sun-accent" role="img" aria-label="Rising sun light glowing from the top right corner"></div>

    <h1 class="podcast-title">
      <span>The</span>
      <span>Mending</span>
      <span>Path</span>
    </h1>

    <div class="listener-figure" role="img" aria-label="Silhouette of a person in profile, head tilted upward toward the sun"></div>

    <div class="brand-signoff">
      <span class="brand-dot"></span>
      <span class="brand-name">LARKSPUR WELLNESS</span>
    </div>
  </main>
</body>
</html>
```